Turm7Zwerge
Zielgruppe
Zielgruppe sind die Eltern, Lehrer, Kindergärtner, aber auch Kinder, die bereits Lesen können.
Aufgabenstellung
Ich brauche einen Flyer und ein Plakat für eine Kinderschachschule für Kinder zwischen 4 und 15 Jahren. Auf dem Flyer, den ich in A6-Format drucken möchte (beidseitig), muss ich die Info über die Kinderschachschule Turm7Zwerge (mehr Infos unter www.turm7zwerge-beispiel.ch), dh., was wir machen, Kontaktdaten, etc schreiben können. Es dient als Werbematerial zum Auslegen
Auf dem Plakat wird mehr oder weniger das Gleiche stehen, es wird jedoch als Din A4 Seite aufgehängt.
Unsere Kontaktinformation ist wie folgt:
Turm7Zwerge: Spielen mit kleinen Strategen
www.turm7zwerge-beispiel.ch

```html
<!DOCTYPE html>
<html lang="de">
<head>
<meta charset="utf-8">
<title>Turm7Zwerge – Warum Kinderschach</title>
<link rel="stylesheet" href="https://fonts.googleapis.com/css2?family=Open+Sans:ital,wght@0,400;0,600;0,700;1,700&display=swap">
<style>
  :root {
    --ochre: #d6981a;
    --cream: #fbf1dc;
    --apricot: #e9b75a;
    --brand-pink: #c2185b;
    --heading-blue: #1f8fc9;
    --heading-pink: #df1f6b;
    --body-text: #2a2a2a;
    --white: #ffffff;
    --paper: #ffffff;
    --paper-tint: #f3f3f3;
  }
  html, body {
    margin: 0;
    padding: 0;
    width: 1200px;
    height: 1200px;
    overflow: hidden;
    background: var(--white);
  }
  .flyer {
    position: relative;
    width: 1200px;
    height: 1200px;
    display: flex;
    font-family: "Open Sans", Arial, sans-serif;
    overflow: hidden;
  }
  .sidebar {
    position: relative;
    width: 362px;
    height: 1200px;
    background: var(--ochre);
    flex: none;
  }
  .brand-panel {
    height: 312px;
    background: linear-gradient(180deg, var(--cream) 0%, var(--apricot) 70%, var(--ochre) 100%);
    display: flex;
    flex-direction: column;
    align-items: center;
    justify-content: center;
    gap: 14px;
  }
  .brand-name {
    display: flex;
    align-items: center;
    gap: 14px;
    font-size: 44px;
    font-weight: 700;
    color: var(--brand-pink);
    letter-spacing: -0.5px;
  }
  .brand-square {
    width: 26px;
    height: 26px;
    background: var(--brand-pink);
  }
  .brand-tagline {
    font-size: 20px;
    font-weight: 700;
    color: var(--brand-pink);
  }
  .photo {
    height: 235px;
    background: linear-gradient(135deg, #3b3a3f 0%, #6b5a4a 45%, #c9b89a 70%, #4a3f38 100%);
  }
  .vertical-url {
    position: absolute;
    left: 32px;
    top: 1135px;
    transform: rotate(-90deg);
    transform-origin: left top;
    white-space: nowrap;
    font-family: Arial, Helvetica, sans-serif;
    font-size: 28px;
    line-height: 36px;
    letter-spacing: 3px;
    color: var(--white);
    opacity: 0.95;
  }
  .contact {
    position: absolute;
    left: 92px;
    top: 782px;
    color: var(--white);
    font-family: Arial, Helvetica, sans-serif;
    font-size: 18px;
    line-height: 30px;
    white-space: nowrap;
  }
  .contact p { margin: 0 0 28px 0; }
  .contact .org-name { font-size: 20px; font-weight: 700; }
  .content {
    position: relative;
    flex: 1;
    background: linear-gradient(180deg, var(--paper) 0%, var(--paper-tint) 100%);
    padding: 88px 34px 0 33px;
    color: var(--body-text);
    font-size: 21px;
    line-height: 30.5px;
    overflow: hidden;
  }
  .content h1, .content h2 {
    margin: 0;
    font-weight: 700;
    line-height: 34px;
  }
  .content h1 {
    font-size: 25px;
    color: var(--heading-blue);
  }
  .content h2 {
    font-size: 23px;
    color: var(--heading-pink);
    margin-top: 28px;
  }
  .content p { margin: 0; hyphens: auto; }
</style>
</head>
<body>
<div class="flyer">
  <aside class="sidebar">
    <div class="brand-panel">
      <div class="brand-name"><span class="brand-square"></span>Turm7Zwerge</div>
      <div class="brand-tagline">Spielen mit kleinen Strategen</div>
    </div>
    <div class="photo" role="img" aria-label="Foto: Zwei Kinder spielen an einem Tisch Schach"></div>
    <div class="vertical-url">www.turm7zwerge-beispiel.ch</div>
    <div class="contact">
      <p><span class="org-name">Turm7Zwerge</span><br>Spielen mit kleinen Strategen<br>Lea Marthaler, Präsidentin</p>
      <p>Lindenweg 12<br>Postfach 418<br>8700 Küsnacht</p>
      <p>Tel.: 079 000 12 34<br>info@turm7zwerge-beispiel.ch<br>www.turm7zwerge-beispiel.ch</p>
    </div>
  </aside>
  <main class="content">
    <h1>Warum Kinderschach:</h1>
    <p>Schach ist weit mehr als ein weiteres Angebot im Dschungel der Kursan&shy;gebote für Kinder. Schach ist eine Lebensschule, die das Leben Ihres Kindes nachhaltig zum Positiven verändern kann. Die Kinder eignen sich spielerisch wesentliche Fähigkeiten an, die sie sowohl im sozialen als auch im schulischen Umfeld zu Höchstleistungen befähigen.</p>
    <h2>1)Schach macht Spass!</h2>
    <p>Schach zieht jeden Spieler sofort in seinen Bann: Kaum ist das Schachbrett aufgebaut und der erste Zug getan, beginnt die Magie zu wirken: Vor den Kindern liegt ein Meer voller aufregender Geschichten. Die spannenden Figuren und intensiven Kämpfe um Sieg und Niederlage wecken den Abenteuergeist der Kinder, ihre Phantasie wird angeregt und lässt die Kinder nicht mehr los. An Spannung schlägt Schach jedes Computerspiel!</p>
    <h2>2)Schach macht schlau und fördert die Konzentrationsfähigkeit</h2>
    <p>Die positive Wirkung von Schachtraining auf die Intelligenz von Kindern ist vielfach belegt und reicht von der Erhöhung kognitiver und sprachlicher Fähigkeiten über eine bessere Leistungs-motivation bis hin zu einer gesteigerten Sozialkompetenz. Die Basis für diesen Leistungsschub liegt in der Stärkung des Konzentrationsvermögens und der Fähigkeit, störende Einflüsse von Aussen auszublenden. Die Kinder lernen, auch bei Zeitdruck einen klaren Kopf zu bewahren und komplexe Problemstellungen auch unter Stress zu bewältigen. Damit verkörpert Schach eine wirksame Mass&shy;nahme gegen Aufmerksamkeitsstörungen und Konzentrationsmängeln bei Kindern.</p>
    <h2>3)Schach macht stark und selbstbewusst!</h2>
    <p>Schach ist lebensnah und vermittelt den Kindern, mit Herausforderungen im Leben konstruktiv umzugehen. Erste Erfolge im Spiel stärken das Selbstvertrauen und der Umgang mit Niederlagen hilft, Verantwortung für die eigenen Züge zu übernehmen und sich mit den eigenen Fehlern auseinanderzusetzen. Damit wird die psychische Stabilität der Kinder und deren Selbstbehauptung gefördert und</p>
  </main>
</div>
</body>
</html>
```